High-end construction company needs a business card design

We need a modern looking business card that draws people in, is memorable and looks so good people will want to sick it on their fridges.
On the first side what is needed are:
Logo
My name - Tomas Verbelk
Title - Managing Director
Website - www.kravel.co.uk
Email - tomas@kravel.co.uk
Telephone - 020 5194 6381
Mobile - 07845319027
On the back side was is needed is a list of all the services we provide:
-Kitchen Renovations
-Bathroom Renovations
-House Renovations
-Garage Conversions
-Extensions
-Loft Conversions
-Conservatories
-Carpentry
-Tiling
-Electrical
-Plumbing & Heating
-Bricklaying
-Landscaping
-Decorating
-Plastering
We would like the colours to be the same shades as on the logo with grey or black for the words.
Target Market(s)
Anyone who needs building work done
Contact Information for Business Card
This business card is for a construction company which strives to deliver excellent service and quality.
The look and feel of the card should represent this.
Requirements
Must have
- On the first side what is needed are:
Logo
My name - Tomas Verbelk
Title - Managing Director
Website - www.kravel.co.uk
Email - tomas@kravel.co.uk
Telephone - 020 5194 6381
Mobile - 07845319027
Nice to have
- Cool looking features

```html
<!DOCTYPE html>
<html lang="en">
<head>
<meta charset="utf-8">
<title>Kravel Construction Ltd – Business Card</title>
<link href="https://fonts.googleapis.com/css2?family=Exo+2:wght@700;800&family=Roboto:wght@400;700;900&display=swap" rel="stylesheet">
<style>
  :root {
    --backdrop: #d8d8d8;
    --card: #ffffff;
    --green: #5cb33f;
    --green-dark: #3e8a3a;
    --green-light: #72c447;
    --ink: #1e1e1e;
    --ink-soft: #333333;
    --rule: #555555;
    --on-green: #ffffff;
  }
  * { margin: 0; padding: 0; box-sizing: border-box; }
  html, body { width: 1200px; height: 800px; overflow: hidden; }
  body {
    background: var(--backdrop);
    position: relative;
    font-family: "Roboto", Arial, sans-serif;
    font-synthesis: none;
  }
  .card {
    position: absolute;
    top: 283px;
    width: 429px;
    height: 237px;
    background: var(--card);
    overflow: hidden;
  }
  .card--front { left: 111px; }
  .card--back { left: 638px; }

  /* brand name */
  .brand-name {
    position: absolute;
    font-family: "Exo 2", Arial, sans-serif;
    font-weight: 800;
    color: var(--green);
    text-transform: uppercase;
    line-height: 1.05;
    letter-spacing: 0.5px;
  }
  .card--front .brand-name { left: 20px; top: 66px; width: 190px; font-size: 18px; }
  .card--back .brand-name { left: 228px; top: 122px; width: 195px; font-size: 19px; }

  /* front */
  .corner-accent { position: absolute; right: 0; top: 0; }
  .divider {
    position: absolute; left: 19px; top: 153px;
    width: 390px; height: 1px; background: var(--rule);
  }
  .contact-list {
    position: absolute; left: 20px; top: 165px;
    list-style: none; font-size: 10.5px; color: var(--ink-soft);
  }
  .contact-list li { display: flex; align-items: center; height: 13.7px; }
  .contact-list svg { width: 9px; height: 9px; margin-right: 8px; fill: var(--green); }
  .person {
    position: absolute; right: 20px; top: 166px; text-align: right;
  }
  .person__name {
    font-weight: 700; font-size: 13px; color: var(--ink); letter-spacing: 0.3px;
  }
  .person__title {
    font-weight: 700; font-size: 9.5px; color: var(--green);
    letter-spacing: 0.8px; margin-top: 3px;
  }
  .footer-line {
    position: absolute; left: 0; bottom: 10px; width: 100%; height: 2px; background: var(--green);
  }
  .footer-band {
    position: absolute; left: 0; bottom: 0; width: 100%; height: 7px; background: var(--green);
  }

  /* back */
  .services-panel { position: absolute; left: 0; top: 0; }
  .services {
    position: absolute; left: 23px; top: 10px; color: var(--on-green);
    font-family: "Roboto", Arial, sans-serif;
  }
  .services__heading {
    font-weight: 700; font-size: 11.5px; letter-spacing: 0.6px;
    margin-bottom: 3px; text-transform: uppercase;
  }
  .services__list {
    list-style: none; font-weight: 700; font-size: 8.6px;
    letter-spacing: 0.55px; text-transform: uppercase;
  }
  .services__list li { display: flex; align-items: center; height: 13.7px; white-space: nowrap; }
  .services__list svg { width: 10px; height: 7px; margin-right: 5px; flex: none; }
</style>
</head>
<body>

<section class="card card--front" aria-label="Business card front">
  <svg class="corner-accent" width="54" height="46" viewBox="0 0 54 46" aria-hidden="true">
    <polygon points="0,0 54,0 54,46" fill="var(--green-light)"/>
    <polygon points="18,0 54,0 54,30" fill="var(--green-dark)" opacity="0.55"/>
  </svg>

  <div class="brand-name">Kravel Construction Ltd</div>

  <div class="divider"></div>

  <ul class="contact-list">
    <li><svg viewBox="0 0 24 24" aria-hidden="true"><path d="M6.6 10.8a15.1 15.1 0 0 0 6.6 6.6l2.2-2.2a1 1 0 0 1 1-.25 11.4 11.4 0 0 0 3.6.57 1 1 0 0 1 1 1V20a1 1 0 0 1-1 1A17 17 0 0 1 3 4a1 1 0 0 1 1-1h3.5a1 1 0 0 1 1 1c0 1.25.2 2.45.57 3.57a1 1 0 0 1-.25 1z"/></svg>020 5194 6381</li>
    <li><svg viewBox="0 0 24 24" aria-hidden="true"><path d="M7 1h10a2 2 0 0 1 2 2v18a2 2 0 0 1-2 2H7a2 2 0 0 1-2-2V3a2 2 0 0 1 2-2zm0 3v14h10V4zm5 15.5a1 1 0 1 0 0 2 1 1 0 0 0 0-2z"/></svg>07845319027</li>
    <li><svg viewBox="0 0 24 24" aria-hidden="true"><path d="M2 5h20v14H2zm2 2v.5l8 5 8-5V7zm0 2.8V17h16V9.8l-8 5z"/></svg>tomas@kravel.co.uk</li>
    <li><svg viewBox="0 0 24 24" aria-hidden="true"><path d="M12 2a10 10 0 1 0 0 20 10 10 0 0 0 0-20zm6.9 6h-2.9a15 15 0 0 0-1.4-3.6A8 8 0 0 1 18.9 8zM12 4a13 13 0 0 1 1.9 4h-3.8A13 13 0 0 1 12 4zM4.3 14a8 8 0 0 1 0-4h3.4a16 16 0 0 0 0 4zm.8 2h2.9a15 15 0 0 0 1.4 3.6A8 8 0 0 1 5.1 16zM8 8H5.1a8 8 0 0 1 4.3-3.6A15 15 0 0 0 8 8zm4 12a13 13 0 0 1-1.9-4h3.8A13 13 0 0 1 12 20zm2.3-6H9.7a14 14 0 0 1 0-4h4.6a14 14 0 0 1 0 4zm.3 5.6a15 15 0 0 0 1.4-3.6h2.9a8 8 0 0 1-4.3 3.6zm1.7-5.6a16 16 0 0 0 0-4h3.4a8 8 0 0 1 0 4z"/></svg>www.kravel.co.uk</li>
  </ul>

  <div class="person">
    <div class="person__name">TOMAS VERBELK</div>
    <div class="person__title">MANAGING DIRECTOR</div>
  </div>

  <div class="footer-line"></div>
  <div class="footer-band"></div>
</section>

<section class="card card--back" aria-label="Business card back">
  <svg class="services-panel" width="429" height="237" viewBox="0 0 429 237" aria-hidden="true">
    <defs>
      <linearGradient id="panelGradient" x1="1" y1="0" x2="0" y2="1">
        <stop offset="0" stop-color="var(--green-dark)"/>
        <stop offset="1" stop-color="var(--green-light)"/>
      </linearGradient>
    </defs>
    <polygon points="0,0 340,0 107,237 0,237" fill="url(#panelGradient)"/>
  </svg>

  <div class="services">
    <h2 class="services__heading">Services we provide</h2>
    <ul class="services__list">
      <li><svg viewBox="0 0 10 7" aria-hidden="true"><polyline points="1,6 5,1.5 9,6" fill="none" stroke="#fff" stroke-width="1.6"/></svg>Kitchen Renovations</li>
      <li><svg viewBox="0 0 10 7" aria-hidden="true"><polyline points="1,6 5,1.5 9,6" fill="none" stroke="#fff" stroke-width="1.6"/></svg>Bathroom Renovations</li>
      <li><svg viewBox="0 0 10 7" aria-hidden="true"><polyline points="1,6 5,1.5 9,6" fill="none" stroke="#fff" stroke-width="1.6"/></svg>House Renovations</li>
      <li><svg viewBox="0 0 10 7" aria-hidden="true"><polyline points="1,6 5,1.5 9,6" fill="none" stroke="#fff" stroke-width="1.6"/></svg>Garage Conversions</li>
      <li><svg viewBox="0 0 10 7" aria-hidden="true"><polyline points="1,6 5,1.5 9,6" fill="none" stroke="#fff" stroke-width="1.6"/></svg>Extensions</li>
      <li><svg viewBox="0 0 10 7" aria-hidden="true"><polyline points="1,6 5,1.5 9,6" fill="none" stroke="#fff" stroke-width="1.6"/></svg>Loft Conversions</li>
      <li><svg viewBox="0 0 10 7" aria-hidden="true"><polyline points="1,6 5,1.5 9,6" fill="none" stroke="#fff" stroke-width="1.6"/></svg>Conservatories</li>
      <li><svg viewBox="0 0 10 7" aria-hidden="true"><polyline points="1,6 5,1.5 9,6" fill="none" stroke="#fff" stroke-width="1.6"/></svg>Carpentry</li>
      <li><svg viewBox="0 0 10 7" aria-hidden="true"><polyline points="1,6 5,1.5 9,6" fill="none" stroke="#fff" stroke-width="1.6"/></svg>Tiling</li>
      <li><svg viewBox="0 0 10 7" aria-hidden="true"><polyline points="1,6 5,1.5 9,6" fill="none" stroke="#fff" stroke-width="1.6"/></svg>Electrical</li>
      <li><svg viewBox="0 0 10 7" aria-hidden="true"><polyline points="1,6 5,1.5 9,6" fill="none" stroke="#fff" stroke-width="1.6"/></svg>Plumbing &amp; Heating</li>
      <li><svg viewBox="0 0 10 7" aria-hidden="true"><polyline points="1,6 5,1.5 9,6" fill="none" stroke="#fff" stroke-width="1.6"/></svg>Bricklaying</li>
      <li><svg viewBox="0 0 10 7" aria-hidden="true"><polyline points="1,6 5,1.5 9,6" fill="none" stroke="#fff" stroke-width="1.6"/></svg>Landscaping</li>
      <li><svg viewBox="0 0 10 7" aria-hidden="true"><polyline points="1,6 5,1.5 9,6" fill="none" stroke="#fff" stroke-width="1.6"/></svg>Decorating</li>
      <li><svg viewBox="0 0 10 7" aria-hidden="true"><polyline points="1,6 5,1.5 9,6" fill="none" stroke="#fff" stroke-width="1.6"/></svg>Plastering</li>
    </ul>
  </div>

  <div class="brand-name">Kravel Construction Ltd</div>
</section>

</body>
</html>
```